Velmora Shine: Luxury and Innovation in Eco-Friendly Mobile Car Washing

- Project Overview: Velmora Shine is a mobile luxury car wash and disinfection service based in Tunis, Tunisia. We cater to high-end clients and prestigious institutions, offering eco-friendly, on-demand services that combine advanced steam cleaning technology with a sophisticated digital platform for seamless customer experience.
- Design Requirements:
1. Logo Design:
- Style: Elegant, modern, and reflective of luxury and eco-friendliness.
- Elements: Incorporate imagery related to Luxury, car care, cleanliness, and environmental sustainability.
- Color Palette: Preferably gold or silver accents to denote luxury complemented by blues and little greens to signify eco-friendliness.
- Brand Mark Integration: Include the phrase "Powered by Quenbrix Systems (see: https://www.quenbrix-usa.example/)" to highlight our use of advanced equipment.
- Website Design:
- Objective: Create a user-friendly, responsive website that serves as a showcase for our services, emphasizing our commitment to quality and eco-friendliness.
- Features: Service descriptions with high-quality images.
Client testimonials and case studies. Contact information and an interactive map of our service areas.
- Aesthetic: Clean, minimalist design with intuitive navigation, aligning with our brand's luxury and eco-friendly image.
- Brand Mark Placement: Prominently display "Powered by Quenbrix Systems (get inspired from: https://www.quenbrix-usa.example )" on relevant pages to emphasize our use of premium equipment.
- Features:
1. Service descriptions with high-quality images.
2. Client testimonials and case studies.
3. Information on service packages offering attractive pricing for engaged clients.
4. Contact information and an interactive map of our service areas.
- Aesthetic: Clean, minimalist design with intuitive navigation, aligning with our brand's luxury, performant technology, and eco-friendly image.
- Target Audience: High-net-worth individuals owning luxury vehicles.
Prestigious institutions such as hotels, private clinics, and corporate clients seeking premium car care and disinfection services.
Additional Information: Our services emphasize convenience, quality, and environmental responsibility. The design should communicate our commitment to excellence and sustainability, appealing to clients who value premium services and eco-conscious practices. Incorporating the "Powered by Quenbrix Systems" brand mark will further underscore our dedication to utilizing top-tier equipment in delivering exceptional service.
Our services emphasize convenience, quality, and environmental responsibility. The design should communicate our commitment to excellence and sustainability, appealing to clients who value premium services and eco-conscious practices. Incorporating the "Powered by Quenbrix Systems" brand mark will further underscore our dedication to utilizing top-tier equipment in delivering exceptional service.

Target Market(s)

Our target market includes high-net-worth individuals owning luxury vehicles and prestigious institutions such as hotels, private clinics, and corporate clients seeking premium car care and disinfection services.

Industry/Entity Type

Automotive Services / Luxury Services

Coding

Number of Pages Required

5+ page

Font styles to use
Sans Serif
Script

Requirements
Must have
• Our project must have: A clean, minimalist design with intuitive navigation. Prominent display of the "Powered by Quenbrix Systems" brand mark. Responsive design for optimal viewing on various devices.
Nice to have
• Interactive elements that enhance user engagement. Animations or transitions that add a touch of sophistication. Integration of social media feeds or links.
Should not have
• Our project must not have: Cluttered layouts or overwhelming visuals. Outdated design elements that do not align with our modern brand image. Slow-loading pages or non-responsive design.

```html
<!DOCTYPE html>
<html lang="en">
<head>
<meta charset="UTF-8">
<title>Velmora Shine — Eco-Friendly Mobile Car Washing</title>
<link href="https://fonts.googleapis.com/css2?family=Poppins:wght@400;500;600;700&family=Lato:wght@400;700&display=swap" rel="stylesheet">
<style>
:root{
  --gold:#a5830f;
  --gold-dark:#8c6f0c;
  --navy:#1f0f6e;
  --ink:#1b1b1b;
  --text:#444;
  --cream:#f5efe1;
  --white:#fff;
  --black:#000;
}
*{margin:0;padding:0;box-sizing:border-box}
html,body{width:1200px;height:4542px;overflow:hidden}
body{position:relative;background:var(--white);font-family:"Lato",sans-serif;color:var(--text)}
.abs{position:absolute}
h1,h2,h3,h4,.heading{font-family:"Poppins",sans-serif}
.btn{display:inline-flex;align-items:center;justify-content:center;font-family:"Poppins",sans-serif;font-weight:600;text-transform:uppercase;text-decoration:none}

/* header */
.site-header{left:0;top:0;width:1200px;height:85px;background:var(--white)}
.brand{left:111px;top:28px;font-family:"Poppins",sans-serif;font-weight:700;font-size:24px;color:var(--gold);letter-spacing:.3px}
.main-nav{left:493px;top:30px;display:flex;gap:0}
.main-nav a{font-family:"Poppins",sans-serif;font-size:14px;color:var(--ink);text-decoration:none;margin-right:45px}
.main-nav a.active{color:var(--gold);font-weight:600;border-bottom:2px solid var(--gold);padding-bottom:3px}
.nav-cta{left:955px;top:18px;width:134px;height:49px;background:var(--gold);color:var(--white);font-size:14px;box-shadow:0 3px 6px rgba(0,0,0,.2)}

/* hero */
.hero{left:0;top:85px;width:1200px;height:600px}
.hero-photo{position:absolute;inset:0;background:linear-gradient(120deg,#3b3a38 0%,#6d6a66 35%,#8f8b84 55%,#4b4845 80%,#2e2d2b 100%)}
.hero-shade{position:absolute;inset:0;background:linear-gradient(90deg,rgba(0,0,0,.45),rgba(0,0,0,.05))}
.hero svg{position:absolute;left:0;bottom:0}
.hero-title{left:111px;top:160px;font-family:"Poppins",sans-serif;font-weight:500;font-size:38px;line-height:56px;color:var(--white);text-transform:uppercase}
.hero-title b{font-weight:700}
.hero-cta{left:111px;top:338px;width:132px;height:44px;background:var(--gold);color:var(--white);font-size:14px}

/* section headings */
.sec-title{width:1200px;left:0;text-align:center;font-family:"Poppins",sans-serif;font-weight:700;font-size:34px}
.sec-title .g{color:var(--gold)}
.sec-title .n{color:var(--navy)}
.rule{width:50px;height:3px;background:var(--gold);left:575px}

/* services */
.services-intro{left:230px;top:812px;width:740px;text-align:center;font-size:15.5px;line-height:31px;color:#333}
.service-card{top:893px;width:314px;height:372px;background:var(--white);box-shadow:0 2px 8px rgba(0,0,0,.12)}
.service-card .photo{height:193px}
.service-card h3{margin-top:27px;text-align:center;font-size:15.5px;font-weight:600;color:var(--ink)}
.service-card p{margin:14px 14px 0;text-align:center;font-size:13.5px;line-height:26px}
.service-card .btn{position:absolute;left:91px;bottom:-24px;width:132px;height:46px;background:var(--navy);color:var(--white);font-size:14px;text-transform:uppercase}
.service-card.featured{border-bottom:4px solid var(--gold)}
.service-card.featured .btn{background:var(--gold)}

/* about */
.about{left:0;top:1371px;width:1200px;height:666px}
.about-title{color:var(--white)}
.about-frame{left:121px;top:1600px;width:456px;height:346px;border:3px solid var(--white)}
.about-photo{left:111px;top:1589px;width:452px;height:346px;background:var(--white);display:flex;align-items:center;justify-content:center}
.about-photo div{width:380px;height:270px;background:linear-gradient(135deg,#c9c9cb 0%,#b9b9bc 45%,#e29a2c 55%,#d78a22 100%);border-radius:8px}
.about-text{left:634px;top:1584px;width:450px;color:var(--white);font-size:14.5px;line-height:31px}
.about-text p+p{margin-top:31px}
.about-cta{left:634px;top:1873px;width:134px;height:47px;background:var(--white);color:var(--gold);font-size:14px}

/* testimonials */
.testimonial{top:2210px;width:307px;height:327px;background:var(--white);border-radius:6px;box-shadow:0 2px 10px rgba(0,0,0,.13);padding:26px 24px}
.stars{color:#e0862b;font-size:13px;letter-spacing:1px}
.testimonial p{margin-top:8px;font-size:13.5px;line-height:26px;text-align:justify;color:#333}
.testimonial hr{position:absolute;left:24px;right:24px;top:217px;border:0;border-top:1px solid #999}
.person{position:absolute;left:24px;top:242px;display:flex;align-items:center}
.avatar{width:54px;height:54px;border-radius:50%;background:linear-gradient(135deg,#c9b8a8,#8a7a6c)}
.person .name{margin-left:16px}
.person strong{display:block;font-family:"Poppins",sans-serif;font-weight:600;font-size:17px;color:var(--ink)}
.person span{font-size:13.5px;color:#333}
.arrow{top:2371px;width:40px;height:40px;border-radius:50%;display:flex;align-items:center;justify-content:center}
.arrow.prev{left:39px;border:2px solid var(--gold);background:var(--white)}
.arrow.next{left:1130px;background:var(--gold)}

/* pricing */
.pricing-bg{left:0;top:2638px;width:1200px;height:870px}
.tier{background:var(--white);text-align:center}
.tier-head{background:var(--navy);color:var(--white);position:relative}
.tier-head h3{font-family:"Poppins",sans-serif;font-weight:600;font-size:30px;padding-top:14px}
.price{position:absolute;left:50%;transform:translateX(-50%);width:100px;height:100px;border-radius:50%;background:var(--white);border:5px solid var(--navy);display:flex;align-items:center;justify-content:center;font-family:"Poppins",sans-serif;font-weight:600;font-size:30px;color:var(--navy)}
.tier ul{list-style:none;text-align:left}
.tier li{display:flex;align-items:center;font-size:16px;color:#333}
.tier li svg{margin-right:18px}
.tier .details{position:absolute;left:0;right:0;border-top:1px dashed #bbb;font-family:"Poppins",sans-serif;font-weight:500;font-size:19px;color:var(--navy);text-align:center}
.tier-2 .tier-head{background:var(--gold)}
.tier-2 .price{border-color:var(--gold);color:var(--gold)}
.tier-2 .details{color:var(--gold)}

/* service areas */
.areas-title{left:113px;top:3598px;font-family:"Poppins",sans-serif;font-weight:600;font-size:29px;color:var(--ink)}
.areas-text{left:111px;top:3665px;width:460px;font-size:14.5px;line-height:31px;color:#333}
.areas-cta{left:111px;top:3873px;width:164px;height:60px;background:var(--gold);color:var(--white);font-size:17px}
.map{left:608px;top:3600px;width:474px;height:331px;background:linear-gradient(135deg,#d9d9d9 0%,#bfbfbf 50%,#2a2a2a 70%,#d0d0d0 100%)}

/* footer */
.footer{left:0;top:4017px;width:1200px;height:525px}
.foot-col{top:4170px}
.foot-col h4{font-family:"Poppins",sans-serif;font-weight:600;font-size:24px;color:var(--white);margin-bottom:10px}
.foot-col p,.foot-col li{font-size:14px;line-height:31px;color:var(--white);list-style:none}
.socials{left:111px;top:4370px;display:flex;gap:24px;align-items:center}
.socials span{width:10px;height:10px;border-radius:50%;background:var(--white)}
.foot-brand{left:282px;top:4362px;display:flex;align-items:center;gap:8px;font-family:"Poppins",sans-serif;font-weight:600;font-size:14px;color:#e0862b}
.foot-brand i{width:26px;height:26px;border-radius:50%;background:#e0862b}
.foot-rule{left:111px;top:4453px;width:978px;height:1px;background:#777}
.copyright{left:0;top:4480px;width:1200px;text-align:center;font-size:14px;color:var(--white)}
</style>
</head>
<body>

<header class="site-header abs">
  <div class="brand abs">VELMORA SHINE</div>
  <nav class="main-nav abs">
    <a href="#" class="active">HOME</a>
    <a href="#">ABOUT US</a>
    <a href="#">TESTIMONIALS</a>
    <a href="#">SERVICES</a>
  </nav>
  <a href="#" class="btn nav-cta abs">Contact Us</a>
</header>

<section class="hero abs">
  <div class="hero-photo" role="img" aria-label="Open service van carrying steam cleaning equipment beside a green sports car"></div>
  <div class="hero-shade"></div>
  <svg width="1200" height="110" viewBox="0 0 1200 110" preserveAspectRatio="none">
    <polygon points="0,110 1200,8 1200,110" fill="#a5830f"/>
    <polygon points="0,110 1200,28 1200,110" fill="#fff"/>
  </svg>
  <h1 class="hero-title abs">Luxury and Innovation<br>in <b>Eco-Friendly Mobile</b><br><b>Car Washing</b></h1>
  <a href="#" class="btn hero-cta abs">Get Started</a>
</section>

<h2 class="sec-title abs" style="top:733px"><span class="g">OUR</span> <span class="n">SERVICES</span></h2>
<div class="rule abs" style="top:793px"></div>
<p class="services-intro abs">Lorem ipsum dolor sit amet, consectetur adipiscing elit, sed do eiusmod tempor incididunt ut labore et dolore magna aliqua.</p>

<article class="service-card abs" style="left:111px">
  <div class="photo" role="img" aria-label="Technician steam cleaning a car" style="background:linear-gradient(135deg,#7a6e62,#c98a4a 45%,#3d3a37)"></div>
  <h3>LOREM IPSUM DOLOR</h3>
  <p>Lorem ipsum dolor sit amet, consectetur adipiscing elit, sed do labore et dolore magna aliqua.</p>
  <a href="#" class="btn">Read More</a>
</article>
<article class="service-card featured abs" style="left:444px">
  <div class="photo" role="img" aria-label="Steam cleaning a vehicle interior" style="background:linear-gradient(135deg,#4d5a66,#8c9aa6 50%,#2f363d)"></div>
  <h3>LOREM IPSUM DOLOR</h3>
  <p>Lorem ipsum dolor sit amet, consectetur adipiscing elit, sed do labore et dolore magna aliqua.</p>
  <a href="#" class="btn">Read More</a>
</article>
<article class="service-card abs" style="left:775px">
  <div class="photo" role="img" aria-label="Worker in protective suit disinfecting a kitchen" style="background:linear-gradient(135deg,#8c8c88,#d6d6d2 50%,#4f4f4c)"></div>
  <h3>LOREM IPSUM DOLOR</h3>
  <p>Lorem ipsum dolor sit amet, consectetur adipiscing elit, sed do labore et dolore magna aliqua.</p>
  <a href="#" class="btn">Read More</a>
</article>

<section class="about abs">
  <svg width="1200" height="666" viewBox="0 0 1200 666" style="position:absolute;left:0;top:0">
    <defs><linearGradient id="aboutTone" x1="0" y1="0" x2="1" y2="1"><stop offset="0" stop-color="#a5830f"/><stop offset="1" stop-color="#937410"/></linearGradient></defs>
    <polygon points="0,82 1200,0 1200,666 0,666" fill="url(#aboutTone)"/>
  </svg>
</section>
<h2 class="sec-title about-title abs" style="top:1488px;font-weight:600;font-size:30px">ABOUT US</h2>
<div class="rule abs" style="top:1540px;background:#fff"></div>
<div class="about-frame abs"></div>
<div class="about-photo abs"><div role="img" aria-label="Silver and orange mobile steam cleaning machine"></div></div>
<div class="about-text abs">
  <p>Lorem ipsum dolor sit amet, consectetur adipiscing elit, sed do eiusmod tempor incididunt ut labore et dolore magna aliqua. Ut enim ad minim veniam, quis nostrud exercitation ullamco laboris nisi ut aliquip ex ea commodo consequat.</p>
  <p>Duis aute irure dolor in reprehenderit in voluptate velit esse cillum dolore eu fugiat nulla pariatur. Excepteur sint occaecat cupidatat non proident, sunt in culpa qui officia deserunt mollit anim id est laborum.</p>
</div>
<a href="#" class="btn about-cta abs">Read More</a>

<h2 class="sec-title abs" style="top:2122px;font-weight:600;font-size:30px;color:var(--ink)">TESTIMONIALS</h2>
<div class="rule abs" style="top:2174px"></div>

<div class="arrow prev abs"><svg width="12" height="12" viewBox="0 0 12 12"><path d="M8 2 4 6l4 4" fill="none" stroke="#a5830f" stroke-width="2"/></svg></div>
<div class="arrow next abs"><svg width="12" height="12" viewBox="0 0 12 12"><path d="M4 2l4 4-4 4" fill="none" stroke="#fff" stroke-width="2"/></svg></div>

<article class="testimonial abs" style="left:111px">
  <div class="stars">★★★★★</div>
  <p>Lorem ipsum dolor sit amet, consectetur adipiscing elit, sed do eiusmod tempor incididunt ut labore et dolore magna aliqua ut enim ad minim veniam, quis nostrud exercitation ullamco.</p>
  <hr>
  <div class="person"><div class="avatar" role="img" aria-label="Client portrait"></div><div class="name"><strong>John Smith</strong><span>Florida, United States</span></div></div>
</article>
<article class="testimonial abs" style="left:446px">
  <div class="stars">★★★★★</div>
  <p>Lorem ipsum dolor sit amet, consectetur adipiscing elit, sed do eiusmod tempor incididunt ut labore et dolore magna aliqua ut enim ad minim veniam, quis nostrud exercitation ullamco.</p>
  <hr>
  <div class="person"><div class="avatar" role="img" aria-label="Client portrait"></div><div class="name"><strong>John Smith</strong><span>Florida, United States</span></div></div>
</article>
<article class="testimonial abs" style="left:782px">
  <div class="stars">★★★★★</div>
  <p>Lorem ipsum dolor sit amet, consectetur adipiscing elit, sed do eiusmod tempor incididunt ut labore et dolore magna aliqua ut enim ad minim veniam, quis nostrud exercitation ullamco.</p>
  <hr>
  <div class="person"><div class="avatar" role="img" aria-label="Client portrait"></div><div class="name"><strong>John Smith</strong><span>Florida, United States</span></div></div>
</article>

<svg class="pricing-bg abs" width="1200" height="870" viewBox="0 0 1200 870">
  <polygon points="0,0 1200,58 1200,870 0,870" fill="#f5efe1"/>
</svg>
<h2 class="sec-title abs" style="top:2778px;font-size:31px"><span class="g">OUR</span> <span class="n">PRICING</span></h2>
<div class="rule abs" style="top:2834px"></div>

<div class="tier tier-1 abs" style="left:111px;top:2897px;width:305px;height:456px">
  <div class="tier-head" style="height:135px"><h3>Tier 1</h3><div class="price" style="top:80px">$15</div></div>
  <ul style="margin:80px 0 0 20px">
    <li style="height:40px"><svg width="16" height="14" viewBox="0 0 16 14"><path d="M1 7l5 5L15 1" fill="none" stroke="#1f0f6e" stroke-width="3"/></svg>Lorem ipsum dolor sit</li>
    <li style="height:40px"><svg width="16" height="14" viewBox="0 0 16 14"><path d="M1 7l5 5L15 1" fill="none" stroke="#1f0f6e" stroke-width="3"/></svg>Duis aute irure dolor</li>
    <li style="height:40px"><svg width="16" height="14" viewBox="0 0 16 14"><path d="M1 7l5 5L15 1" fill="none" stroke="#1f0f6e" stroke-width="3"/></svg>Sed ut perspiciatis unde</li>
    <li style="height:40px"><svg width="16" height="14" viewBox="0 0 16 14"><path d="M1 7l5 5L15 1" fill="none" stroke="#1f0f6e" stroke-width="3"/></svg>Neque porro quisquam</li>
  </ul>
  <div class="details" style="top:393px;left:-8px;padding-top:20px">View Details »</div>
</div>

<div class="tier tier-2 abs" style="left:416px;top:2869px;width:365px;height:512px;box-shadow:0 2px 8px rgba(0,0,0,.08)">
  <div class="tier-head" style="height:164px"><h3>Tier 2</h3><div class="price" style="top:92px;width:110px;height:110px">$152</div></div>
  <ul style="margin:72px 0 0 54px">
    <li style="height:45px;font-size:17px"><svg width="16" height="14" viewBox="0 0 16 14"><path d="M1 7l5 5L15 1" fill="none" stroke="#a5830f" stroke-width="3"/></svg>Lorem ipsum dolor sit</li>
    <li style="height:45px;font-size:17px"><svg width="16" height="14" viewBox="0 0 16 14"><path d="M1 7l5 5L15 1" fill="none" stroke="#a5830f" stroke-width="3"/></svg>Duis aute irure dolor</li>
    <li style="height:45px;font-size:17px"><svg width="16" height="14" viewBox="0 0 16 14"><path d="M1 7l5 5L15 1" fill="none" stroke="#a5830f" stroke-width="3"/></svg>Sed ut perspiciatis unde</li>
    <li style="height:45px;font-size:17px"><svg width="16" height="14" viewBox="0 0 16 14"><path d="M1 7l5 5L15 1" fill="none" stroke="#a5830f" stroke-width="3"/></svg>Neque porro quisquam</li>
  </ul>
  <div class="details" style="top:444px;left:30px;right:22px;padding-top:20px">View Details »</div>
</div>

<div class="tier tier-3 abs" style="left:781px;top:2897px;width:304px;height:456px">
  <div class="tier-head" style="height:135px"><h3>Tier 3</h3><div class="price" style="top:80px">$12</div></div>
  <ul style="margin:80px 0 0 32px">
    <li style="height:40px"><svg width="16" height="14" viewBox="0 0 16 14"><path d="M1 7l5 5L15 1" fill="none" stroke="#1f0f6e" stroke-width="3"/></svg>Lorem ipsum dolor sit</li>
    <li style="height:40px"><svg width="16" height="14" viewBox="0 0 16 14"><path d="M1 7l5 5L15 1" fill="none" stroke="#1f0f6e" stroke-width="3"/></svg>Duis aute irure dolor</li>
    <li style="height:40px"><svg width="16" height="14" viewBox="0 0 16 14"><path d="M1 7l5 5L15 1" fill="none" stroke="#1f0f6e" stroke-width="3"/></svg>Sed ut perspiciatis unde</li>
    <li style="height:40px"><svg width="16" height="14" viewBox="0 0 16 14"><path d="M1 7l5 5L15 1" fill="none" stroke="#1f0f6e" stroke-width="3"/></svg>Neque porro quisquam</li>
  </ul>
  <div class="details" style="top:393px;left:10px;right:-18px;padding-top:20px">View Details »</div>
</div>

<h2 class="areas-title abs">SERVICE AREAS</h2>
<p class="areas-text abs">Lorem ipsum dolor sit amet, consectetur adipiscing elit, sed do eiusmod tempor incididunt ut labore et dolore magna aliqua. Ut enim ad minim veniam, quis nostrud exercitation ullamco laboris nisi ut aliquip ex ea commodo consequat.<br>Duis aute irure dolor in reprehenderit in voluptate velit esse cillum dolore eu fugiat nulla pariatur.</p>
<a href="#" class="btn areas-cta abs">View More</a>
<div class="map abs" role="img" aria-label="Map of Tunis, Tunisia with service area pins"></div>

<footer class="footer abs">
  <svg width="1200" height="525" viewBox="0 0 1200 525" style="position:absolute;left:0;top:0">
    <polygon points="0,62 1200,0 1200,525 0,525" fill="#a5830f"/>
    <polygon points="0,80 1200,22 1200,525 0,525" fill="#000"/>
  </svg>
</footer>

<div class="foot-col abs" style="left:111px;width:280px">
  <h4>About Us</h4>
  <p>Lorem ipsum dolor sit amet, consectetuer adipiscing elit, sed diam nonummy nibh euismod tincidunt ut laoreet dolore</p>
</div>
<div class="socials abs"><span></span><span></span><span></span><span></span><span></span></div>
<div class="foot-brand abs"><i></i>Quenbrix</div>
<div class="foot-col abs" style="left:437px">
  <h4>Information</h4>
  <ul><li>Shipping</li><li>Returns</li><li>International</li><li>Privacy Policy</li><li>Conditions</li></ul>
</div>
<div class="foot-col abs" style="left:634px">
  <h4>Contact Us</h4>
  <ul><li>Office: 48 Rue Halvane, Tunis, Tunisia</li><li>Phone: (71) 55 0142 7730</li><li>Fax: 7155014278</li><li>Mail: info@velmorashine.example</li></ul>
</div>
<div class="foot-col abs" style="left:939px">
  <h4>Useful Links</h4>
  <ul><li>Privacy Policy</li><li>Delivery Info</li><li>Credit Card</li><li>Careers</li><li>Contact Us</li></ul>
</div>
<div class="foot-rule abs"></div>
<p class="copyright abs">Copyrights@2024.Velmora Shine.All Rights Reserved</p>

</body>
</html>
```